Stated Income Loans

Flyer design to be used on social media platforms (i.e. Chatterbox, Snapgrove etc.)

Target Market(s)

Real Estate Investors

Requirements
Must have
• INVESTOR STATED INCOME LOANS
• "IT'S TIME TO THINK BIG"
• * Purchase or Refinance up to 3 Million
• * No Income Docs or Bank Statements
• * Vacant Properties Allowed
• * Minimum Credit Score 620
• * Cash Out up to 80%
• Same Day Pre-Approval
• 20-30 Day Close
• Call Marcus Whitfield today...
• Bluecrest Lending Group, Inc.
• Phone (800) 641-2957 x 17
• Direct (240) 958-2074
• www.bluecrestlendhub.com
• NMLS #583617 / #47081
Should not have
• Do not use same color scheme as website. Be creative.

```html
<!DOCTYPE html>
<html lang="en">
<head>
<meta charset="utf-8">
<title>Investor Stated Income Loans Flyer</title>
<link href="https://fonts.googleapis.com/css2?family=Jost:wght@400;500;600;700&display=swap" rel="stylesheet">
<style>
  :root {
    --maroon: #a1332f;
    --rust: #b4561f;
    --blush: #f7e8ea;
    --ink: #111111;
    --grey-text: #474747;
    --brand-blue: #1f4e9c;
    --white: #ffffff;
    --page-bg: #d9d9d9;
    --accent-gradient: linear-gradient(90deg, #9b2f41 0%, #b5591d 100%);
  }
  * { margin: 0; padding: 0; box-sizing: border-box; }
  html, body { width: 1200px; height: 1200px; overflow: hidden; }
  body { background: var(--page-bg); font-family: "Jost", Arial, sans-serif; }
  .flyer {
    position: absolute; left: 177px; top: 20px;
    width: 845px; height: 1160px;
    background: var(--white); overflow: hidden;
  }
  .abs { position: absolute; }

  /* header */
  .header-brand { left: 34px; top: 20px; display: flex; align-items: center; gap: 12px; }
  .brand-dot { width: 36px; height: 36px; border-radius: 50%; background: var(--maroon); }
  .header-brand .brand-name {
    font-size: 13px; font-weight: 600; color: var(--maroon); line-height: 15px; text-transform: uppercase;
  }
  .social { left: 668px; top: 22px; text-align: center; }
  .social-label { font-size: 5px; font-weight: 600; color: var(--maroon); letter-spacing: 0.1px; text-transform: uppercase; }
  .social-icons { display: flex; gap: 15px; margin-top: 7px; }
  .social-icons span { width: 18px; height: 18px; border: 1.5px solid var(--maroon); border-radius: 50%; }

  /* hero */
  .hero-photo {
    left: 0; top: 78px; width: 845px; height: 375px;
    background: linear-gradient(180deg, #d8d8d8 0%, #9a9a9a 35%, #5a5a5a 70%, #2e2e2e 100%);
  }
  .blush-band { left: 0; top: 453px; width: 845px; height: 345px; background: var(--blush); }

  .card-shadow {
    left: 60px; top: 520px; width: 725px; height: 60px;
    background: radial-gradient(ellipse at 50% 0%, rgba(0,0,0,0.35) 0%, rgba(0,0,0,0) 65%);
  }
  .headline-card {
    left: 62px; top: 331px; width: 719px; height: 193px;
    background: var(--white); border-radius: 22px;
  }
  .card-divider { left: 421px; top: 345px; width: 2px; height: 147px; background: var(--maroon); }
  .headline-left {
    right: 446px; top: 392px; text-align: right; white-space: nowrap;
    font-size: 31px; font-weight: 700; color: var(--maroon); line-height: 34px; letter-spacing: 0.6px;
    text-transform: uppercase;
  }
  .headline-right { left: 446px; top: 384px; color: var(--maroon); font-weight: 700; }
  .headline-right .quote { position: absolute; left: 0; top: -2px; font-size: 40px; line-height: 40px; }
  .headline-right .line1 { padding-left: 36px; font-size: 38px; line-height: 40px; letter-spacing: 0.8px; white-space: nowrap; }
  .headline-right .line2 { padding-left: 36px; font-size: 47px; line-height: 48px; letter-spacing: 0.6px; white-space: nowrap; }

  .tab-shadow {
    left: 300px; top: 344px; width: 245px; height: 26px;
    background: radial-gradient(ellipse at 50% 0%, rgba(0,0,0,0.45) 0%, rgba(0,0,0,0) 70%);
  }
  .cash-tab {
    left: 302px; top: 239px; width: 239px; height: 105px;
    background: var(--accent-gradient); color: var(--white);
    display: flex; flex-direction: column; justify-content: center; align-items: center;
    font-size: 22px; font-weight: 600; line-height: 22px; letter-spacing: 0.8px; text-transform: uppercase;
  }

  .offer-title {
    left: 0; top: 572px; width: 845px; text-align: center;
    font-size: 26px; font-weight: 700; color: var(--ink); letter-spacing: 1px;
  }
  .feature { top: 650px; font-size: 19px; font-weight: 600; color: var(--grey-text); line-height: 28px; letter-spacing: 0.6px; text-transform: uppercase; }
  .feature-vacant { right: 582px; text-align: right; }
  .feature-docs { left: 288px; width: 266px; text-align: center; }
  .feature-credit { left: 570px; }
  .feature-divider { top: 638px; width: 1.5px; height: 100px; background: #c6a3a8; }

  /* closing */
  .badge-shadow {
    left: 250px; top: 859px; width: 343px; height: 28px;
    background: radial-gradient(ellipse at 50% 0%, rgba(0,0,0,0.4) 0%, rgba(0,0,0,0) 70%);
  }
  .close-badge {
    left: 252px; top: 787px; width: 339px; height: 72px; border-radius: 3px;
    background: var(--accent-gradient); color: var(--white); text-align: center;
    display: flex; flex-direction: column; justify-content: center;
    text-transform: uppercase; letter-spacing: 1px;
  }
  .close-badge .days { font-size: 19px; font-weight: 400; line-height: 24px; }
  .close-badge .approval { font-size: 18px; font-weight: 600; line-height: 24px; }
  .contact-divider { left: 421px; top: 859px; width: 2px; height: 223px; background: var(--maroon); }

  .lender-brand { left: 48px; top: 925px; display: flex; align-items: center; gap: 22px; }
  .lender-brand .brand-name {
    font-size: 21px; font-weight: 600; color: var(--brand-blue); line-height: 24px; text-transform: uppercase;
  }
  .lender-brand .brand-dot { width: 64px; height: 64px; background: var(--brand-blue); }

  .call-block { left: 484px; top: 929px; text-transform: uppercase; }
  .call-block .small { font-size: 14px; font-weight: 600; color: #3a3a3a; line-height: 18px; letter-spacing: 0.5px; }
  .call-block .name { font-size: 20px; font-weight: 700; color: var(--maroon); line-height: 21px; letter-spacing: 0.5px; }
  .agent-photo {
    left: 633px; top: 905px; width: 124px; height: 124px; border-radius: 50%;
    background: radial-gradient(circle at 50% 35%, #6b7f99 0%, #3b4a5e 55%, #1c1c20 100%);
  }

  /* footer */
  .footer {
    left: 0; top: 1082px; width: 845px; height: 79px;
    background: var(--accent-gradient); color: var(--white);
  }
  .footer-item { position: absolute; display: flex; align-items: center; font-size: 14px; line-height: 19px; }
  .footer-item svg { margin-right: 14px; flex: none; }
  .footer-item b { font-weight: 600; }
  .footer-phone { left: 50px; top: 21px; }
  .footer-web { left: 312px; top: 30px; }
  .footer-nmls { left: 557px; top: 30px; }
</style>
</head>
<body>
<main class="flyer">
  <header>
    <div class="abs header-brand">
      <span class="brand-dot"></span>
      <div class="brand-name">Bluecrest<br>Lending Group,<br>Inc.</div>
    </div>
    <div class="abs social">
      <div class="social-label">Find us on social media</div>
      <div class="social-icons"><span></span><span></span><span></span></div>
    </div>
  </header>

  <div class="abs hero-photo" role="img" aria-label="Black and white photo of business people silhouetted against a city skyline through large office windows"></div>
  <div class="abs blush-band"></div>

  <div class="abs card-shadow"></div>
  <div class="abs headline-card"></div>
  <div class="abs card-divider"></div>
  <h1 class="abs headline-left">Investor Stated<br>Income Loans</h1>
  <div class="abs headline-right">
    <span class="quote">“</span>
    <div class="line1">IT'S TIME TO</div>
    <div class="line2">THINK BIG</div>
  </div>

  <div class="abs tab-shadow"></div>
  <div class="abs cash-tab"><span>Cash Out</span><span>Up to 80%</span></div>

  <h2 class="abs offer-title">PURCHASE OR REFINANCE UP TO 3 MILLION</h2>
  <div class="abs feature feature-vacant">Vacant Properties<br>Allowed</div>
  <div class="abs feature-divider" style="left:287px"></div>
  <div class="abs feature feature-docs">No Income Docs<br>or Bank Statements</div>
  <div class="abs feature-divider" style="left:553px"></div>
  <div class="abs feature feature-credit">Minimum Credit<br>Score 620</div>

  <div class="abs badge-shadow"></div>
  <div class="abs close-badge">
    <span class="days">20-30 Day Close</span>
    <span class="approval">Same Day Pre-Approval</span>
  </div>
  <div class="abs contact-divider"></div>

  <div class="abs lender-brand">
    <div class="brand-name">Bluecrest<br>Lending Group,<br>Inc.</div>
    <span class="brand-dot" style="border-radius:50%"></span>
  </div>

  <div class="abs call-block">
    <div class="small">Call</div>
    <div class="name">Marcus<br>Whitfield</div>
    <div class="small">Today</div>
  </div>
  <div class="abs agent-photo" role="img" aria-label="Portrait photo of loan officer Marcus Whitfield in a dark suit"></div>

  <footer class="abs footer">
    <div class="footer-item footer-phone">
      <svg width="28" height="28" viewBox="0 0 28 28" fill="none" stroke="#fff" stroke-width="1.5">
        <circle cx="14" cy="14" r="12.5"/>
        <path d="M10 8.5l2.5 0 1 3-1.6 1.2c.8 1.8 2 3 3.4 3.6l1.3-1.6 3 1v2.6c-5.5.4-10-4-9.6-9.8z" fill="#fff" stroke="none"/>
      </svg>
      <div>PHONE <b>(800) 641-2957 X 17</b><br>DIRECT <b>(240) 958-2074</b></div>
    </div>
    <div class="footer-item footer-web">
      <svg width="28" height="28" viewBox="0 0 28 28" fill="none" stroke="#fff" stroke-width="1.4">
        <circle cx="14" cy="14" r="12"/>
        <ellipse cx="14" cy="14" rx="5.5" ry="12"/>
        <path d="M2 14h24M4 8h20M4 20h20"/>
      </svg>
      <span>www.bluecrestlendhub.com</span>
    </div>
    <div class="footer-item footer-nmls">
      <svg width="22" height="26" viewBox="0 0 22 26" fill="none" stroke="#fff" stroke-width="1.5">
        <path d="M11 24s-8-8.5-8-14a8 8 0 0116 0c0 5.5-8 14-8 14z"/>
        <circle cx="11" cy="10" r="3"/>
      </svg>
      <span>NMLS #583617 / #47081</span>
    </div>
  </footer>
</main>
</body>
</html>
```